Bluewater Ridge Commercial Svcs

I need a business card for my company in Orlando Florida. I provide all property maintenance/repair services both commercial and residential. We also do kitchen and bath remodels, full gut rehab and renovation, and painting. I do not have any suggestions for card layout. I want something that looks great that i can hand out to contractors and home owners to help generate business.

Target Market(s)

contractors, property owners, real estate property managers

Industry/Entity Type

Business

Contact Information for Business Card

Bluewater Ridge Commercial Services, Dale Morrow, 2186 Tamsey Ln. Orlando,FL 32811, Owner

```html
<!DOCTYPE html>
<html lang="en">
<head>
<meta charset="UTF-8">
<title>Bluewater Ridge Commercial Services – Business Card</title>
<link rel="stylesheet" href="https://fonts.googleapis.com/css2?family=Lato:wght@700;900&family=Montserrat:wght@400&display=swap">
<style>
  :root {
    --navy: #13216e;
    --navy-frame: #1b2a78;
    --black: #050505;
    --green: #2fbf5a;
    --grey: #6b6b6b;
    --white: #ffffff;
    --backdrop: #e9e9eb;
  }
  * { margin: 0; padding: 0; box-sizing: border-box; }
  html, body { width: 1200px; height: 900px; overflow: hidden; background: var(--backdrop); }
  .card {
    position: absolute; left: 100px; top: 164px;
    width: 1000px; height: 572px;
    background: var(--white);
    overflow: hidden;
    box-shadow: 0 10px 30px rgba(0,0,0,.18);
    font-family: "Lato", sans-serif;
  }
  .owner { position: absolute; left: 48px; top: 118px; }
  .owner-name { color: var(--green); font-weight: 900; font-size: 30px; letter-spacing: .5px; line-height: 1; }
  .owner-role { color: var(--grey); font-weight: 900; font-size: 19px; letter-spacing: 1px; line-height: 1.05; }
  .region-map {
    position: absolute; right: 40px; top: 26px; width: 220px; height: 120px;
    border-radius: 30px 8px 60px 10px;
    background: linear-gradient(135deg, #e5f7ea, #c9efd4);
  }
  .project { position: absolute; top: 168px; width: 320px; text-align: center; }
  .project.before { left: 175px; }
  .project.after { left: 535px; }
  .project-photo {
    width: 320px; height: 180px; border-radius: 22px;
    border: 5px solid var(--navy-frame);
    box-shadow: 0 0 0 2px #fff, 0 0 0 4px var(--navy-frame);
  }
  .before .project-photo { background: linear-gradient(180deg, #9fb4c0 0%, #5f6e55 40%, #7d8180 70%, #56794a 100%); }
  .after .project-photo { background: linear-gradient(180deg, #a7bccb 0%, #58704b 38%, #c9cbc4 65%, #5e8a45 100%); }
  .project-label { color: var(--navy); font-weight: 900; font-size: 22px; margin-top: 6px; letter-spacing: .5px; }
  .info-band {
    position: absolute; left: 0; top: 386px; width: 100%; height: 140px;
    background: var(--navy); color: var(--white); text-align: center;
    padding-top: 8px;
  }
  .company-name { font-weight: 900; font-size: 34px; letter-spacing: .5px; line-height: 1.1; }
  .services { font-weight: 900; font-size: 21px; line-height: 1.3; }
  .address {
    font-family: "Montserrat", sans-serif; font-weight: 400; font-size: 22px;
    letter-spacing: 1.5px; margin-top: 4px;
    display: flex; justify-content: center; align-items: center; gap: 12px;
  }
  .address svg { width: 24px; height: 22px; fill: var(--white); }
  .base-band { position: absolute; left: 0; top: 526px; width: 100%; height: 46px; background: var(--black); }
</style>
</head>
<body>
  <main class="card">
    <div class="region-map" role="img" aria-label="Outline map of the state of Florida"></div>

    <div class="owner">
      <div class="owner-name">DALE MORROW</div>
      <div class="owner-role">OWNER</div>
    </div>

    <figure class="project before">
      <div class="project-photo" role="img" aria-label="House and driveway before cleaning"></div>
      <figcaption class="project-label">BEFORE</figcaption>
    </figure>
    <figure class="project after">
      <div class="project-photo" role="img" aria-label="House and driveway after cleaning"></div>
      <figcaption class="project-label">AFTER</figcaption>
    </figure>

    <section class="info-band">
      <h1 class="company-name">BLUEWATER RIDGE COMMERCIAL SERVICES</h1>
      <p class="services">Property Maintenance / Repair Services for Commercial &amp; Residential</p>
      <p class="services">kitchen &amp; Bath Remodels,&nbsp; Full Gut Rehab &amp; Renovation &amp; Painting</p>
      <p class="address">
        <svg viewBox="0 0 24 22" aria-hidden="true"><path d="M12 1 1 11h3v10h6v-6h4v6h6V11h3z"/></svg>
        2186 Tamsey Ln. Orlando,FL 32811
      </p>
    </section>
    <div class="base-band"></div>
  </main>
</body>
</html>
```